Kestrel vale motors

I’m looking for artwork that can go on the back of my vehicles that I sell. It’s going to be a magnet on the back of the vehicle. On the magnet it needs to state - I am for sale!
Please visit - kestrelvalemotors.com

And in all caps - WE BEAT ANY PRICE!

Logo attached

Car sales

Car sales

```html
<!DOCTYPE html>
<html lang="en">
<head>
<meta charset="utf-8">
<title>Kestrel Vale Motors – I Am For Sale Magnet</title>
<link rel="stylesheet" href="https://fonts.googleapis.com/css2?family=Anton&family=Archivo+Black&display=swap">
<style>
  :root {
    --paper: #ffffff;
    --dome-red: #ec1f26;
    --dome-light: #f0575c;
    --panel-black: #231f20;
    --burst-deep: #7a1230;
    --burst-red: #b21f2d;
    --sale-yellow: #fff000;
    --brand-white: #ffffff;
  }
  html, body {
    margin: 0;
    padding: 0;
    width: 1200px;
    height: 1000px;
    overflow: hidden;
    background: var(--paper);
  }
  .magnet {
    display: block;
    width: 1200px;
    height: 1000px;
  }
  .dome-ring { fill: var(--dome-red); }
  .dome-inner { fill: url(#domeGlow); }
  .brand-name {
    font-family: "Anton", sans-serif;
    fill: var(--brand-white);
    font-size: 84px;
  }
  .brand-web {
    font-family: "Anton", sans-serif;
    fill: var(--brand-white);
    font-size: 40px;
  }
  .sign-panel { fill: var(--panel-black); }
  .burst { fill: url(#burstGlow); }
  .headline { fill: var(--sale-yellow); }
  .headline-wide { font-family: "Archivo Black", sans-serif; }
  .headline-condensed { font-family: "Anton", sans-serif; }
</style>
</head>
<body>
<svg class="magnet" viewBox="0 0 1200 1000" xmlns="http://www.w3.org/2000/svg">
  <defs>
    <radialGradient id="domeGlow" cx="50%" cy="100%" r="100%">
      <stop offset="0%" stop-color="#ec3a40"/>
      <stop offset="60%" stop-color="var(--dome-light)"/>
      <stop offset="100%" stop-color="#ef4a50"/>
    </radialGradient>
    <radialGradient id="burstGlow" cx="50%" cy="50%" r="50%">
      <stop offset="0%" stop-color="var(--burst-deep)"/>
      <stop offset="55%" stop-color="var(--burst-red)"/>
      <stop offset="100%" stop-color="var(--panel-black)" stop-opacity="0"/>
    </radialGradient>
    <clipPath id="domeClip">
      <rect x="0" y="0" width="1200" height="456"/>
    </clipPath>
    <clipPath id="panelClip">
      <polygon points="241,452 958,452 857,914 339,914"/>
    </clipPath>
  </defs>

  <!-- Brand dome -->
  <g class="brand-dome" clip-path="url(#domeClip)">
    <circle class="dome-ring" cx="600" cy="460" r="358"/>
    <circle class="dome-inner" cx="600" cy="460" r="328" role="img" aria-label="Sunburst of light red rays radiating from the bottom of the dome"/>
  </g>
  <text class="brand-name" x="600" y="270" text-anchor="middle" textLength="350" lengthAdjust="spacingAndGlyphs">KESTREL VALE</text>
  <text class="brand-name" x="600" y="358" text-anchor="middle" textLength="230" lengthAdjust="spacingAndGlyphs">MOTORS</text>
  <text class="brand-web" x="600" y="428" text-anchor="middle" textLength="392" lengthAdjust="spacingAndGlyphs">KESTRELVALEMOTORS.COM</text>

  <!-- Sale panel -->
  <polygon class="sign-panel" points="241,451 959,451 958,459 857,914 339,914 243,459"/>
  <g clip-path="url(#panelClip)">
    <ellipse class="burst" cx="600" cy="690" rx="390" ry="260" role="img" aria-label="Red starburst rays behind the sale lettering"/>
  </g>

  <text class="headline headline-wide" x="273" y="551" font-size="92" textLength="653" lengthAdjust="spacingAndGlyphs">I AM FOR</text>
  <text class="headline headline-wide" x="295" y="661" font-size="108" textLength="609" lengthAdjust="spacingAndGlyphs">SALE</text>
  <text class="headline headline-condensed" x="313" y="762" font-size="92" textLength="574" lengthAdjust="spacingAndGlyphs">WE BEAT ANY</text>
  <text class="headline headline-wide" x="334" y="874" font-size="120" textLength="532" lengthAdjust="spacingAndGlyphs">PRICES!</text>
</svg>
</body>
</html>
```